Simple and clean

We need a business card design for a new company called Dwelling Owl. It is a search engine to find current properties for sale or rent in New Zealand market.
We have already a colour scheme that we would like people to use.
Light brown: #D4CCB0
Light green: #D6E4D4
Green: #669966
Black/White
It is OK to divert from this colour scheme slightly as long as there is a green component to the business card.
Final design should be clean, simple and should communicate the nature of the business.
Target Market(s)
- First home buyers
- Real estate agents
- People seeking rentals
Industry/Entity Type
Business
Requirements
Must have
- Use those or similar colours.
Light brown: #D4CCB0
Light green: #D6E4D4
Green: #669966
Black/White

```html
<!DOCTYPE html>
<html lang="en">
<head>
<meta charset="utf-8">
<title>Dwelling Owl – Business Card</title>
<link rel="stylesheet" href="https://fonts.googleapis.com/css2?family=Source+Sans+3:wght@400;600;700&display=swap">
<style>
  :root {
    --backdrop: #d4dfd2;
    --card: #ffffff;
    --brand-green: #3b7139;
    --ink: #1e1e1e;
    --on-green: #ffffff;
  }
  html, body {
    margin: 0;
    padding: 0;
    width: 1200px;
    height: 900px;
    overflow: hidden;
    background: var(--backdrop);
    font-family: "Source Sans 3", sans-serif;
  }
  .canvas {
    position: relative;
    width: 1200px;
    height: 900px;
  }
  .business-card {
    position: absolute;
    left: 232px;
    top: 240px;
    width: 736px;
    height: 420px;
    background: var(--card);
    box-shadow: inset 0 0 34px 8px rgba(0, 0, 0, 0.38);
    overflow: hidden;
  }
  .brand {
    position: absolute;
    left: 30px;
    top: 172px;
    display: flex;
    align-items: center;
    gap: 10px;
  }
  .brand-mark {
    width: 30px;
    height: 30px;
    background: var(--brand-green);
  }
  .brand-name {
    font-weight: 700;
    font-size: 32px;
    color: var(--brand-green);
    line-height: 1;
  }
  .name-band {
    position: absolute;
    left: 298px;
    top: 152px;
    width: 438px;
    height: 90px;
    background: var(--brand-green);
    color: var(--on-green);
    text-align: right;
    box-sizing: border-box;
    padding: 10px 32px 0 0;
  }
  .person-name {
    margin: 0;
    font-weight: 700;
    font-size: 33px;
    line-height: 1.15;
  }
  .person-role {
    margin: 0;
    font-weight: 400;
    font-size: 23px;
    line-height: 1.2;
  }
  .contact-list {
    position: absolute;
    right: 22px;
    top: 308px;
    margin: 0;
    padding: 0;
    list-style: none;
  }
  .contact-item {
    display: flex;
    justify-content: flex-end;
    align-items: center;
    gap: 8px;
    height: 32px;
    font-size: 23px;
    color: var(--ink);
  }
  .contact-tag {
    width: 22px;
    height: 22px;
    background: var(--brand-green);
    color: var(--on-green);
    font-size: 14px;
    font-weight: 700;
    display: flex;
    align-items: center;
    justify-content: center;
  }
</style>
</head>
<body>
  <main class="canvas">
    <section class="business-card">
      <div class="brand">
        <span class="brand-mark"></span>
        <span class="brand-name">Dwelling Owl</span>
      </div>

      <div class="name-band">
        <p class="person-name">Mara Whitcombe</p>
        <p class="person-role">Director</p>
      </div>

      <ul class="contact-list">
        <li class="contact-item"><span>+000-000-0000</span><span class="contact-tag">T</span></li>
        <li class="contact-item"><span>mara@dwellingowl.co.nz</span><span class="contact-tag">E</span></li>
        <li class="contact-item"><span>www.dwellingowl.co.nz</span><span class="contact-tag">W</span></li>
      </ul>
    </section>
  </main>
</body>
</html>
```